Sonstige Design für Bild mit Produktvorteilen
Zielgruppe
Herstellung und Vertrieb von Kinderspieltürmen für den Garten.
Aufgabenstellung
Wir suchen ein Bild was Produktvorteile darstellt. Das Bild soll als zusätzlichen Produktbild in unserem Shop / Tauschly / Marktora verwendet werden.
Vorteile:
- 10 Jahre Garantie
- Extra dicke Pofosten 9 x 9 cm
- Premium Holz glatt gehobelt
- Kesseldruckimprägniert, kein streichen notwendig
Beispielpordukt: https://www.kolbensteg.net/green-otter-spielturm-sand-cove-mit-rutsche-2-30-m-rampe-mit-seil

```html
<!DOCTYPE html>
<html lang="de">
<head>
<meta charset="utf-8">
<title>Spielturm Sand Cove – Vorteile</title>
<link rel="stylesheet" href="https://fonts.googleapis.com/css2?family=Open+Sans:ital,wght@0,400;0,600;0,700;1,600&family=Kalam:wght@400&display=swap">
<style>
  :root {
    --band-green: #2f4a14;
    --icon-green: #6b9a2c;
    --accent-orange: #ec8a1c;
    --text-dark: #3a3a3a;
    --white: #ffffff;
  }
  html, body { margin: 0; padding: 0; overflow: hidden; }
  body { width: 1200px; height: 739px; background: var(--white); font-family: "Open Sans", sans-serif; }
  .canvas { position: relative; width: 1200px; height: 739px; overflow: hidden; background: var(--white); }
  .header-band { position: absolute; left: 0; top: 0; width: 1200px; height: 232px; background: var(--band-green); }
  .title { position: absolute; left: 492px; top: 32px; margin: 0; font-size: 46px; font-weight: 600; color: var(--white); letter-spacing: 0.5px; }
  .title em { font-style: italic; font-weight: 600; }
  .subtitle { position: absolute; left: 496px; top: 100px; margin: 0; font-size: 38px; font-weight: 700; color: var(--accent-orange); }
  .product-visual { position: absolute; left: 20px; top: 40px; width: 470px; height: 699px;
    background: linear-gradient(160deg, #b89a6c 0%, #a88a5c 45%, #7fb43a 75%, #d9c9a2 100%); border-radius: 6px; }
  .benefits { position: absolute; left: 530px; top: 318px; margin: 0; padding: 0; list-style: none; }
  .benefit { position: relative; display: flex; align-items: flex-start; height: 104px; margin-bottom: 6px; }
  .benefit-icon { width: 74px; height: 74px; flex: none; margin-right: 34px; }
  .benefit-title { display: block; font-size: 36px; font-weight: 400; color: var(--text-dark); line-height: 44px; }
  .benefit-note { display: block; font-family: "Kalam", cursive; font-size: 32px; color: var(--accent-orange); line-height: 36px; }
  .benefit-first { align-items: center; height: 80px; margin-bottom: 22px; }
</style>
</head>
<body>
<div class="canvas">
  <div class="header-band"></div>
  <h1 class="title">Spielturm <em>SAND COVE</em></h1>
  <p class="subtitle">Vorteile auf einen Blick:</p>
  <div class="product-visual" role="img" aria-label="Illustration eines hölzernen Spielturms mit grüner Rutsche und spielenden Kindern"></div>

  <ul class="benefits">
    <li class="benefit benefit-first">
      <svg class="benefit-icon" viewBox="0 0 74 74" aria-hidden="true">
        <path d="M24 48 L16 70 L26 64 L31 72 L36 52 Z M50 48 L58 70 L48 64 L43 72 L38 52 Z" fill="var(--icon-green)"/>
        <circle cx="37" cy="30" r="27" fill="var(--icon-green)"/>
        <circle cx="37" cy="30" r="20" fill="none" stroke="#fff" stroke-width="3"/>
        <path d="M27 30 L34 37 L48 23" fill="none" stroke="var(--accent-orange)" stroke-width="6" stroke-linecap="round" stroke-linejoin="round"/>
      </svg>
      <span class="benefit-title">10 Jahre Garantie</span>
    </li>
    <li class="benefit">
      <svg class="benefit-icon" viewBox="0 0 74 74" aria-hidden="true">
        <rect x="27" y="4" width="20" height="66" rx="4" fill="var(--icon-green)"/>
        <path d="M31 16 H43 M31 30 H43 M31 44 H43 M31 58 H43" stroke="#fff" stroke-width="2"/>
      </svg>
      <div><span class="benefit-title">Extra dicke Pfosten</span><span class="benefit-note">9x9 cm</span></div>
    </li>
    <li class="benefit">
      <svg class="benefit-icon" viewBox="0 0 74 74" aria-hidden="true">
        <path d="M6 24 L40 12 L68 22 L34 34 Z" fill="var(--icon-green)"/>
        <path d="M6 24 L34 34 L34 48 L6 38 Z" fill="#4f7a1c"/>
        <path d="M34 34 L68 22 L68 36 L34 48 Z" fill="#85b345"/>
        <path d="M6 42 L34 52 L34 64 L6 54 Z" fill="#4f7a1c"/>
        <path d="M34 52 L68 40 L68 52 L34 64 Z" fill="#85b345"/>
      </svg>
      <div><span class="benefit-title">Premium Holz</span><span class="benefit-note">glatt gehobelt</span></div>
    </li>
    <li class="benefit">
      <svg class="benefit-icon" viewBox="0 0 74 74" aria-hidden="true">
        <path d="M6 36 Q37 0 68 36 Q60 30 52 36 Q44 30 37 36 Q30 30 22 36 Q14 30 6 36 Z" fill="var(--accent-orange)"/>
        <path d="M37 36 V62 Q37 70 29 68" fill="none" stroke="var(--icon-green)" stroke-width="4" stroke-linecap="round"/>
        <path d="M20 50 v6 M54 48 v6 M46 60 v6" stroke="var(--icon-green)" stroke-width="3" stroke-linecap="round"/>
      </svg>
      <div><span class="benefit-title">Kesseldruckimprägniert</span><span class="benefit-note">kein Streichen notwendig</span></div>
    </li>
  </ul>
</div>
</body>
</html>
```